Copperfork Roundtable Podcast

We need a Podcast Cover design that is compatible with Apple Podcasts, Spotify, etc. In this podcast, we interview the real movers & shakers in the foodservice industry who cut through the noise to get to the top.

```html
<!DOCTYPE html>
<html lang="en">
<head>
<meta charset="utf-8">
<title>Copperfork Roundtable Podcast — Cover</title>
<link rel="stylesheet" href="https://fonts.googleapis.com/css2?family=Raleway:wght@200;400&display=swap">
<style>
  :root {
    --band-gold: #c8bf86;
    --ink-white: #ffffff;
    --room-dark: #14110d;
    --room-warm: #5a4a2c;
    --room-amber: #a8893f;
    --room-teal: #2f3a33;
  }
  html, body {
    margin: 0;
    padding: 0;
    width: 1200px;
    height: 1200px;
    overflow: hidden;
    background: var(--room-dark);
  }
  .cover {
    position: relative;
    width: 1200px;
    height: 1200px;
    overflow: hidden;
    font-family: "Raleway", sans-serif;
  }
  .band {
    position: absolute;
    left: 0;
    width: 1200px;
    background: var(--band-gold);
  }
  .band--top { top: 0; height: 50px; }
  .band--bottom { bottom: 0; height: 50px; }
  .host-photo {
    position: absolute;
    top: 50px;
    left: 0;
    width: 1200px;
    height: 1100px;
    background:
      radial-gradient(ellipse 420px 520px at 760px 420px, rgba(120,100,70,0.55), rgba(0,0,0,0) 70%),
      radial-gradient(ellipse 380px 300px at 220px 480px, rgba(168,137,63,0.55), rgba(0,0,0,0) 70%),
      linear-gradient(90deg, var(--room-warm) 0%, var(--room-teal) 45%, #1c2330 70%, var(--room-warm) 100%);
  }
  .host-photo::after {
    content: "";
    position: absolute;
    inset: 0;
    background: linear-gradient(180deg, rgba(0,0,0,0) 45%, rgba(10,8,6,0.75) 100%);
  }
  .show-title {
    position: absolute;
    left: 190px;
    top: 190px;
    margin: 0;
    color: var(--ink-white);
    font-weight: 400;
    font-size: 74px;
    line-height: 0.95;
    letter-spacing: 1px;
  }
  .show-title span { display: block; }
  .show-title .line-two { padding-left: 40px; }
  .host-name {
    position: absolute;
    left: 0;
    top: 0;
    width: 1200px;
    height: 1200px;
  }
  .host-name text {
    fill: var(--ink-white);
    font-family: "Raleway", sans-serif;
    font-weight: 200;
  }
  .host-name .with-label {
    font-weight: 400;
    font-size: 34px;
    letter-spacing: 4px;
  }
</style>
</head>
<body>
  <main class="cover">
    <div class="host-photo" role="img" aria-label="Photo of the smiling host in a navy blazer and light blue shirt, seated in a warmly lit restaurant dining room"></div>
    <div class="band band--top"></div>
    <div class="band band--bottom"></div>

    <h1 class="show-title">
      <span class="line-one">Copperfork</span>
      <span class="line-two">Roundtable</span>
    </h1>

    <svg class="host-name" viewBox="0 0 1200 1200" aria-label="with Dario Velasco">
      <text class="with-label" x="168" y="840">WITH</text>
      <text x="360" y="882" font-size="225" textLength="480" lengthAdjust="spacingAndGlyphs">DARIO</text>
      <text x="66" y="1098" font-size="225" textLength="1068" lengthAdjust="spacing">VELASCO</text>
    </svg>
  </main>
</body>
</html>
```